Halvorsen Plumbing LLC business card

Would like a modern looking business card with my new logo

Contact Information for Business Card

Dwight Halvorsen 2417 Birchmont Hollow Rd Alderbrook Falls, QX 06512, Halvorsenplumbingllc@mailnest.example, 555-555-0184

```html
<!DOCTYPE html>
<html lang="en">
<head>
<meta charset="utf-8">
<title>Halvorsen Plumbing LLC – Business Card</title>
<link href="https://fonts.googleapis.com/css2?family=Michroma&family=Montserrat:wght@600;700&display=swap" rel="stylesheet">
<style>
  :root {
    --stage: #2b2b2d;
    --card-white: #ffffff;
    --brand-blue: #0aa6e6;
    --ink: #141414;
    --rule: #1c1c1c;
  }
  * { box-sizing: border-box; margin: 0; padding: 0; }
  html, body {
    width: 1200px;
    height: 1108px;
    overflow: hidden;
    background: var(--stage);
  }
  .stage {
    position: relative;
    width: 1200px;
    height: 1108px;
    display: flex;
    justify-content: center;
    align-items: center;
    gap: 80px;
  }
  .card {
    width: 400px;
    height: 680px;
    border-radius: 26px;
    overflow: hidden;
    position: relative;
  }
  /* Front */
  .card-front {
    background: var(--card-white);
    display: flex;
    flex-direction: column;
    align-items: center;
    text-align: center;
  }
  .wordmark {
    margin-top: 150px;
    font-family: "Michroma", sans-serif;
    color: var(--ink);
    line-height: 1.1;
  }
  .wordmark-name { display: block; font-size: 38px; letter-spacing: 1px; }
  .wordmark-sub { display: block; font-size: 15px; letter-spacing: 5px; margin-top: 8px; }
  .contact {
    margin-top: 180px;
    font-family: "Montserrat", sans-serif;
    font-weight: 700;
    color: var(--ink);
    display: flex;
    flex-direction: column;
    align-items: center;
  }
  .contact-name {
    font-family: "Michroma", sans-serif;
    color: var(--brand-blue);
    font-size: 22px;
    letter-spacing: 1px;
  }
  .contact-rule {
    width: 70px;
    height: 1.5px;
    background: var(--rule);
    margin: 14px 0;
  }
  .contact-line { font-size: 16px; line-height: 1.45; letter-spacing: 0.5px; }
  .contact-email { font-size: 14px; letter-spacing: 0.3px; }
  /* Back */
  .card-back {
    background: var(--brand-blue);
    display: flex;
    align-items: center;
    justify-content: center;
  }
  .back-pattern {
    position: absolute;
    inset: 0;
    background: linear-gradient(135deg, #12ace9 0%, #0aa3e2 50%, #0c9fdc 100%);
  }
  .back-mark {
    position: relative;
    font-family: "Michroma", sans-serif;
    color: var(--card-white);
    font-size: 34px;
    letter-spacing: 1px;
  }
</style>
</head>
<body>
  <main class="stage">
    <section class="card card-front" aria-label="Business card front">
      <div class="wordmark">
        <span class="wordmark-name">HALVORSEN</span>
        <span class="wordmark-sub">PLUMBING LLC</span>
      </div>
      <div class="contact">
        <p class="contact-name">DWIGHT HALVORSEN</p>
        <span class="contact-rule"></span>
        <p class="contact-line">2417 Birchmont Hollow Rd</p>
        <p class="contact-line">Alderbrook Falls, QX 06512</p>
        <span class="contact-rule"></span>
        <p class="contact-line">555-555-0184</p>
        <p class="contact-line contact-email">Halvorsenplumbingllc@mailnest.example</p>
      </div>
    </section>
    <section class="card card-back" aria-label="Business card back">
      <div class="back-pattern" role="img" aria-label="Tone-on-tone repeated company name pattern in blue"></div>
      <p class="back-mark">HALVORSEN</p>
    </section>
  </main>
</body>
</html>
```